PLVMS Business Card and Stationary Project

A new business card and stationary design.
It would be ideal to tie into the design concept of our new logo.
It would be nice if the business card could be sophisticated and eye-catching. Having a 2 sided card. Perhaps logo only on one side, and details on the other side.
- Consider muting the intensity of the logo to improve the sophistication level.
The logo with the HK city skyscrapers behind is a secondary logo only. If used, may overcomplicate the card / stationary.
When designing the stationary, please keep it sophisticated and understated. I would consider the philosophy of less is more.
As an option, perhaps muting the strong colour tones of the logo.
Target Market(s)
Airline industry management and executives
Industry/Entity Type
Business
Contact Information for Business Card
2 sided clean and professional business card.
Colors
Designer to choose colors to be used in the design.
Requirements
Must have
- The new PLVMS logo, see below
- Name
- Position
- Address
- Phone number
- email address
- Office address for letterhead / card
- Meridian Flightdeck Staff Guild
- 8/F Corlan Tower, 12-14 Wexbury Lane, Fennick Bay, Kowloon, Hong Kong
- Tel: +852 2419 5582 Fax: +852 2419 5617 Email: plvms@plvms-mail.example
- GRUMET logo
- TriStar Flightdeck Staff alliance logo
- BRNEVU Logo ( getting vector file)
Nice to have
- For the business card:
- Less necessary:
- Member of Worldwide Council of Cabin Navigators Unions
- Member of Tristar Flightdeck Staff Alliance
- English one side, Chinese text back side (will provide) - Might be too cluttered
- For the stationary:
- GRUMTE and TFSA logos not necessary.

```html
<!DOCTYPE html>
<html lang="en">
<head>
<meta charset="utf-8">
<title>PLVMS Business Card</title>
<link href="https://fonts.googleapis.com/css2?family=Roboto:wght@400;500;900&display=swap" rel="stylesheet">
<style>
  :root {
    --stage: #1f1f1f;
    --card: #f7f7f7;
    --card-edge: #e9e9e9;
    --brand-blue: #1f56a8;
    --brand-red: #e3262d;
    --ink: #2b2b2b;
    --muted-blue: #a9b9d6;
    --rule: #555;
    --badge-grey: #b8bec8;
  }
  html, body {
    margin: 0;
    width: 1200px;
    height: 545px;
    overflow: hidden;
    background: var(--stage);
    font-family: "Roboto", Arial, sans-serif;
  }
  .stage { position: relative; width: 1200px; height: 545px; }
  .card {
    position: absolute;
    top: 114px;
    height: 310px;
    background: linear-gradient(180deg, #ffffff 0%, var(--card) 60%, var(--card-edge) 100%);
    overflow: hidden;
    box-shadow: 0 4px 10px rgba(0,0,0,.45);
  }
  .card--front { left: 55px; width: 535px; }
  .card--back { left: 622px; width: 530px; }

  /* front */
  .front-mark {
    position: absolute;
    left: 0; right: 0; top: 128px;
    display: flex; align-items: center; justify-content: center; gap: 14px;
  }
  .front-mark__dot { width: 16px; height: 16px; border-radius: 50%; background: var(--brand-red); }
  .front-mark__name { font-weight: 900; font-size: 58px; letter-spacing: 2px; color: var(--brand-blue); line-height: 1; }
  .front-guild {
    position: absolute; left: 0; right: 0; top: 196px;
    text-align: center; font-weight: 500; font-size: 13px; letter-spacing: .5px;
    color: var(--brand-red); text-transform: uppercase;
  }

  /* back */
  .bands { position: absolute; inset: 0; }
  .holder { position: absolute; left: 28px; top: 52px; color: #fff; }
  .holder__name { font-size: 16px; font-weight: 500; line-height: 18px; }
  .holder__title { font-size: 13px; color: var(--muted-blue); line-height: 16px; }
  .back-mark {
    position: absolute; left: 254px; top: 44px;
    font-weight: 900; font-size: 46px; letter-spacing: 1px; color: var(--brand-blue); line-height: 1;
  }
  .back-guild {
    position: absolute; left: 256px; top: 93px;
    font-size: 10.5px; font-weight: 500; color: var(--brand-red); text-transform: uppercase; letter-spacing: .2px;
  }
  .contacts { position: absolute; margin: 0; padding: 0; list-style: none; font-size: 12px; color: var(--ink); }
  .contacts li { display: flex; align-items: center; gap: 6px; height: 16px; }
  .contacts svg { width: 11px; height: 11px; flex: none; }
  .contacts--personal { left: 28px; top: 103px; }
  .contacts--office { left: 28px; top: 194px; }
  .divider { position: absolute; left: 30px; right: 27px; top: 186px; height: 1px; background: var(--rule); }
  .address { position: absolute; left: 294px; top: 195px; display: flex; gap: 6px; font-size: 12px; line-height: 16px; color: var(--ink); }
  .address svg { width: 10px; height: 14px; margin-top: 1px; }
  .memberships {
    position: absolute; left: 29px; top: 273px; margin: 0; padding: 0; list-style: none;
    font-size: 10.5px; line-height: 15px; color: #fff;
  }
  .partner-badge--round {
    position: absolute; left: 362px; top: 240px; width: 40px; height: 40px; border-radius: 50%;
    background: radial-gradient(circle, #dfe6f2 0 45%, var(--brand-blue) 46% 60%, var(--badge-grey) 61%);
  }
  .partner-badge--wing {
    position: absolute; left: 344px; top: 256px; width: 76px; height: 8px; background: var(--badge-grey); border-radius: 4px; z-index: -1;
  }
  .partner-badge--square {
    position: absolute; left: 440px; top: 248px; width: 64px; height: 34px;
    background: linear-gradient(180deg, #dfe6f2 0 30%, var(--brand-blue) 30%);
  }
</style>
</head>
<body>
<main class="stage">

  <section class="card card--front" aria-label="Card front">
    <div class="front-mark">
      <span class="front-mark__dot"></span>
      <span class="front-mark__name">PLVMS</span>
    </div>
    <div class="front-guild">Meridian Flightdeck Staff Guild</div>
  </section>

  <section class="card card--back" aria-label="Card back">
    <svg class="bands" viewBox="0 0 530 310" width="530" height="310" aria-hidden="true">
      <polygon points="0,44 212,44 194,82 0,82" fill="var(--brand-blue)"/>
      <polygon points="216,44 224,44 206,82 198,82" fill="var(--brand-red)"/>
      <polygon points="228,44 236,44 218,82 210,82" fill="var(--brand-red)"/>
      <polygon points="358,296 530,296 530,310 366,310" fill="var(--brand-red)"/>
      <polygon points="0,268 348,268 364,310 0,310" fill="var(--brand-blue)"/>
    </svg>

    <div class="holder">
      <div class="holder__name">Captain Aldous Renner</div>
      <div class="holder__title">Plvms Chairman</div>
    </div>

    <div class="back-mark">PLVMS</div>
    <div class="back-guild">Meridian Flightdeck Staff Guild</div>

    <ul class="contacts contacts--personal">
      <li><svg viewBox="0 0 10 14"><rect x="1" y="0.5" width="8" height="13" rx="1.5" fill="none" stroke="var(--brand-red)" stroke-width="1.4"/><circle cx="5" cy="11" r="0.9" fill="var(--brand-red)"/></svg>+852 614 3307</li>
      <li><svg viewBox="0 0 12 9"><rect width="12" height="9" fill="var(--brand-red)"/><path d="M0 0 6 5 12 0" fill="none" stroke="#fff" stroke-width="1.2"/></svg>info@meridiangroup.example</li>
      <li><svg viewBox="0 0 12 12"><circle cx="6" cy="6" r="5.2" fill="none" stroke="var(--brand-red)" stroke-width="1.2"/><ellipse cx="6" cy="6" rx="2.3" ry="5.2" fill="none" stroke="var(--brand-red)"/><path d="M1 6h10" stroke="var(--brand-red)"/></svg>www.plvms.example</li>
    </ul>

    <div class="divider"></div>

    <ul class="contacts contacts--office">
      <li><svg viewBox="0 0 12 10"><path d="M1 4c0-3 10-3 10 0l-2 1-1-2H4L3 5z" fill="var(--brand-red)"/><rect x="3" y="5" width="6" height="5" rx="1" fill="var(--brand-red)"/></svg>+852 2419 5582</li>
      <li><svg viewBox="0 0 12 11"><rect x="3" y="0" width="6" height="3" fill="var(--brand-red)"/><rect x="0" y="3.5" width="12" height="5" rx="1" fill="var(--brand-red)"/><rect x="3" y="7" width="6" height="4" fill="var(--brand-red)" stroke="#fff" stroke-width=".8"/></svg>+852 2419 5617</li>
      <li><svg viewBox="0 0 12 9"><rect width="12" height="9" fill="var(--brand-red)"/><path d="M0 0 6 5 12 0" fill="none" stroke="#fff" stroke-width="1.2"/></svg>plvms@plvms-mail.example</li>
    </ul>

    <div class="address">
      <svg viewBox="0 0 10 14"><path d="M5 14S0 7.5 0 5a5 5 0 0 1 10 0c0 2.5-5 9-5 9z" fill="var(--brand-red)"/><circle cx="5" cy="5" r="1.8" fill="#fff"/></svg>
      <span>8/F Corlan Tower, 12 Wexbury Lane<br>Fennick Bay, Hong Kong</span>
    </div>

    <div class="partner-badge--wing" role="img" aria-label="Partner alliance badge"></div>
    <div class="partner-badge--round" role="img" aria-label="Tristar Flightdeck Staff Alliance badge"></div>
    <div class="partner-badge--square" role="img" aria-label="GRUMET badge"></div>

    <ul class="memberships">
      <li>Member of Worldwide Council of Cabin Navigators Unions</li>
      <li>Member of Tristar Flightdeck Staff Alliance</li>
    </ul>
  </section>

</main>
</body>
</html>
```